Business Card Design Project

Hi

I have a draft of a business card which I need smarting up. I have attached the pdf of this.
The information on the front is correct.
The information on the back should contain:
Project Management, Consulting, Master Systems Integrator, Datacenter, Relocations, Restacks. I want this spiraling around the back

Can you change the telephone number to +65 8574 3916.
Updates

Target Market(s)

Chief Technology Officers of large multi-nationals

Industry/Entity Type

Business

Requirements
Must have
• My logo - Vorlith (attached)
The orange and blue colour running around the edge

```html
<!DOCTYPE html>
<html lang="en">
<head>
<meta charset="utf-8">
<title>Vorlith Business Card Concepts</title>
<link rel="stylesheet" href="https://fonts.googleapis.com/css2?family=Source+Sans+3:wght@400;500&display=swap">
<style>
  :root {
    --ink: #111111;
    --paper: #ffffff;
    --orange: #f28a1e;
    --blue: #5cc6d8;
    --mark: #0d0d0d;
  }
  * { box-sizing: border-box; margin: 0; padding: 0; }
  html, body { width: 1200px; height: 720px; overflow: hidden; background: var(--paper); }
  body { position: relative; font-family: "Source Sans 3", "Myriad Pro", sans-serif; color: var(--ink); }

  .card {
    position: absolute;
    width: 432px;
    height: 241px;
    background: var(--paper);
    border: 2px solid var(--ink);
  }
  .card::before {
    content: "";
    position: absolute;
    inset: 2px;
    border: 1px solid var(--orange);
  }
  .card--dual::before {
    box-shadow: inset 0 0 0 1px var(--blue);
  }

  .card--front-a { left: 157px; top: 106px; }
  .card--back-a  { left: 612px; top: 106px; }
  .card--front-b { left: 157px; top: 408px; }
  .card--back-b  { left: 612px; top: 408px; }

  .brand-square {
    position: absolute;
    left: 24px; top: 27px;
    width: 133px; height: 130px;
    background: var(--mark);
    border-radius: 20px;
  }
  .brand-name {
    position: absolute;
    left: 177px; top: 62px;
    font-size: 58px;
    font-weight: 400;
    line-height: 1;
    letter-spacing: 1px;
    color: var(--ink);
  }

  .person { position: absolute; left: 24px; top: 156px; line-height: 1; }
  .person__name { font-size: 20px; letter-spacing: 0.6px; }
  .person__role { font-size: 18px; margin-top: 2px; }

  .details {
    position: absolute;
    left: 24px; top: 200px;
    font-size: 12.6px;
    line-height: 16.3px;
    white-space: nowrap;
  }

  .services-spiral {
    position: absolute;
    left: 0; top: 0;
    width: 428px; height: 237px;
  }
  .services-spiral__guide { fill: none; stroke: none; }
  .services-spiral__text {
    font-family: "Source Sans 3", "Myriad Pro", sans-serif;
    font-size: 13px;
    letter-spacing: 0.3px;
    fill: var(--ink);
  }
</style>
</head>
<body>

  <section class="card card--front-a">
    <div class="brand-square"></div>
    <div class="brand-name">Vorlith</div>
    <div class="person">
      <p class="person__name">Daniel Harrow</p>
      <p class="person__role">Director</p>
    </div>
    <div class="details">
      <p>Vorlith Pte Ltd, 21 Harbour Crest, #09-12 Lumen Point Tower 2, Singapore</p>
      <p>T: +65 8574 3916&nbsp; E: daniel.harrow@vorlith.com&nbsp;&nbsp; W: www.vorlith.com</p>
    </div>
  </section>

  <section class="card card--back-a">
    <svg class="services-spiral" viewBox="0 0 428 237">
      <path id="spiral-a" class="services-spiral__guide"
        d="M64,118 A150,95 0 0 1 364,118 A141,86 0 0 1 82,118 A132,77 0 0 1 346,118 A123,68 0 0 1 100,118 A114,59 0 0 1 328,118"/>
      <text class="services-spiral__text"><textPath href="#spiral-a">Project Management • Consulting • Master Systems Integrator • Datacenter • Relocations • Restacks</textPath></text>
    </svg>
  </section>

  <section class="card card--dual card--front-b">
    <div class="brand-square"></div>
    <div class="brand-name">Vorlith</div>
    <div class="person">
      <p class="person__name">Daniel Harrow</p>
      <p class="person__role">Director</p>
    </div>
    <div class="details">
      <p>Vorlith Pte Ltd, 21 Harbour Crest, #09-12 Lumen Point Tower 2, Singapore</p>
      <p>T: +65 8574 3916&nbsp; E: daniel.harrow@vorlith.com&nbsp;&nbsp; W: www.vorlith.com</p>
    </div>
  </section>

  <section class="card card--dual card--back-b">
    <svg class="services-spiral" viewBox="0 0 428 237">
      <path id="spiral-b" class="services-spiral__guide"
        d="M64,118 A150,95 0 0 1 364,118 A141,86 0 0 1 82,118 A132,77 0 0 1 346,118 A123,68 0 0 1 100,118 A114,59 0 0 1 328,118"/>
      <text class="services-spiral__text"><textPath href="#spiral-b">Project Management • Consulting • Master Systems Integrator • Datacenter • Relocations • Restacks</textPath></text>
    </svg>
  </section>

</body>
</html>
```